Landing Page für B2B-Softwareentwicklungsfirma
Zielgruppe
Wir sind eine (relativ kleine) B2B Softwareentwicklungsfirma, die Software zum Wetten auf Pferderennen erstellt.
Unsere Kunden sind Buchmacher und Rennbahnbetreiber.
Unsere Software läuft auf verschiedener Hardware (Touchscreen Terminals, Handy, Kassa, Webseite,...) und wird teilweise von Endkunden (Sportwetter) als auch Kunden-Mitarbeitern verwendet.
Was uns von anderen Softwarefirmen in diesem Bereich unterscheidet ist:
- Wir sind extrem verlässlich und unsere Software läuft störungsfrei
- Wir haben extrem viel Knowhow und ein großes Netzwerk im Bereich Pferdesport/-wetten
- Wir sind flexibel, gehen auf Kundenwünsche immer schnell und kosteneffizient ein
- Unsere softwaretechnischen Fähigkeiten sind ausgezeichnet (wir sind hauptsächlich Programmierer - weniger Businessleute).
- Wir sind für unsere Kunden immer persönlich, direkt und einfach ansprechbar (kleine Firma)
- Wir sind seit ca 15 Jahren erfolgreich im Markt, und auch Marktführer im deutschsprachigen Raum
- Wir haben ein sehr breites Produktportfolio (Terminal, Kassa, Mobile Webseite, Desktop Webseite, Backoffice, Risk Management)
- Wir legen viel Wert auf sauberes und auch modernes UI/UX-Design
Wir benötigen nun einen professionellen Webauftritt um in neue Märkte einzutreten.
Als ersten Schritt möchten wir gerne eine Single-Page Landingpage, die alle wichtigen Punkte im Überblick darstellt.
Aufgabenstellung
Das Design soll die Punkte aus der obigen Beschreibung über uns widerspiegeln, und auch unsere Werte:
Wichtig: Modern, Verlässlichkeit, Dynamisch, Kosteneffizient, Freundlich
Optional: Kreativ, Flexibilität
Wichtig ist auch der Bezug zum Pferderennsport!
Und dass wir eine B2B Softwarefirma sind!
Bitte beachten Sie unser neues Firmenlogo - siehe Anhang.
Die Landingpage soll eher hell, klar, offen, freundlich, sachlich sein.
Die Landingpage soll auf Mobile und Desktop funktionieren und gut aussehen.
Bitte verwenden Sie folgende Gliederung der Landingpage:
Sections:
....* Above the fold
........headline: horse betting software
........subheadline: Multi-product betting solution for bookmakers and racetrack operators.
................................Software production for land-based operations and online betting.
........call-to-action: get in touch
........secondary call-to-action: view products
........switch language
........links to other sections
....* Products
........Point of Sale
............Title: Quick and streamlined bet placement
............Short desc: Optimized bet placement solution for your bet shops and race tracks. Supports Windows-based touchscreen terminals and many different printers and scanners out of the box.
........Self-Service Terminals
............Title: Let users take control
............Short desc: Easy to use touchscreen software for new and professional punters. Running on any Windows-based hardware and adapted to your special needs.
........Web and Mobile Betting
............Title: Reach your target audience wherever they are
............Short desc: Allow your customers to enter their bets on any desktop or mobile browser.
........Bet Management
............Title: Stay in control of your meetings and bets
............Short desc: Browser-based Back-Office solution to control all your meetings,..

```html
<!DOCTYPE html>
<html lang="en">
<head>
<meta charset="utf-8">
<title>Brightmoor – Horse Betting Software Provider</title>
<link rel="stylesheet" href="https://fonts.googleapis.com/css2?family=Poppins:wght@400;500;600;700;800&display=swap">
<style>
:root{
  --ink:#2a2a2a;
  --text:#333;
  --muted:#8a8f9a;
  --navy:#0a5688;
  --cyan:#2cc4e4;
  --hero-a:#f4f8fd;
  --hero-b:#cfeef8;
  --line:#e6eaf2;
  --card-border:#e3e8f5;
  --blue:#3c5ee8;
  --red:#ec3563;
  --orange:#f5a72e;
  --teal:#36d6b4;
  --dot:#3ed0a2;
}
*{box-sizing:border-box;margin:0;padding:0}
html,body{width:1200px;height:2326px;overflow:hidden}
body{font-family:"Poppins",sans-serif;color:var(--text);background:#fff;position:relative}
.abs{position:absolute}
.hero-bg{left:0;top:0;width:1200px;height:860px}
.brand{left:24px;top:32px;font-size:28px;font-weight:500;letter-spacing:2px;color:var(--ink)}
.nav{left:419px;top:40px;display:flex;gap:19px;font-size:15.5px;color:var(--ink)}
.lang{left:975px;top:40px;font-size:15.5px;color:#555}
.btn{display:inline-flex;align-items:center;justify-content:center;background:var(--navy);color:#fff;border-radius:26px;font-size:16px;font-weight:500;height:48px}
.contact{left:1068px;top:29px;width:113px;height:45px;font-size:16px}
.eyebrow{left:24px;top:198px;font-size:17px;font-weight:600;color:var(--cyan)}
.hero-title{left:24px;top:242px;font-size:63px;font-weight:800;line-height:77px;color:var(--ink);letter-spacing:-0.5px}
.hero-copy{left:24px;top:516px;width:490px;font-size:18px;line-height:29px;color:var(--ink)}
.cta-primary{left:24px;top:665px;width:189px}
.cta-link{left:245px;top:677px;font-size:16px;color:var(--navy);text-decoration:underline}
.hero-photo{left:754px;top:206px;width:324px;height:324px;border-radius:12px;background:linear-gradient(160deg,#a9b6a2,#8a6a4c 55%,#c5a27c);box-shadow:0 6px 18px rgba(0,0,0,.12)}
.hero-terminal{left:842px;top:416px;width:328px;height:272px;border-radius:12px;background:linear-gradient(135deg,#2a3a3e,#7f9f8a 60%,#c9d9cc);box-shadow:0 6px 18px rgba(0,0,0,.15)}
.section-title{left:0;width:1200px;text-align:center;top:930px;font-size:47px;font-weight:800;color:var(--ink)}
.section-sub{left:300px;width:620px;text-align:center;top:1028px;font-size:18px;line-height:29px;color:var(--ink)}
.product-title{font-size:31px;font-weight:800;color:var(--ink)}
.product-copy{font-size:18px;line-height:29px;color:var(--ink);width:580px}
.features{display:flex;gap:22px}
.feature{width:166px;height:134px;border:2px solid var(--card-border);border-radius:22px;display:flex;flex-direction:column;align-items:center;justify-content:flex-start;padding-top:18px;font-size:17px;color:var(--ink)}
.feature svg{width:48px;height:48px;margin-bottom:14px}
.more{width:183px}
.card{background:#fff;border:1px solid var(--line);border-radius:6px}
.card-head{font-size:15px;font-weight:600;color:var(--ink);padding:17px 18px;border-bottom:1px solid var(--line)}
.small{font-size:11px;color:var(--muted)}
</style>
</head>
<body>

<svg class="abs hero-bg" viewBox="0 0 1200 860" aria-hidden="true">
  <defs><linearGradient id="hg" x1="0" y1="0" x2="1" y2="1"><stop offset="0" stop-color="#f5f8fd"/><stop offset=".55" stop-color="#eef6fc"/><stop offset="1" stop-color="#c6ecf7"/></linearGradient></defs>
  <path d="M0 0H1200V735C980 790 700 850 440 852C260 853 110 830 0 790Z" fill="url(#hg)"/>
</svg>

<header>
  <div class="abs brand">BRIGHTMOOR</div>
  <nav class="abs nav"><span>Products</span><span>Why us?</span><span>Company &amp; Team</span><span>FAQ</span></nav>
  <div class="abs lang">DE / EN</div>
  <a class="abs btn contact">Contact</a>
</header>

<section class="hero">
  <div class="abs eyebrow">HORSE BETTING SOFTWARE PROVIDER</div>
  <h1 class="abs hero-title">The Reliable Way<br>To Manage<br>Your Races</h1>
  <p class="abs hero-copy">We provide multi-product betting solutions for bookmakers and racetrack operators. Our proven software products are a perfect fit for land-based as well as online betting operations.</p>
  <a class="abs btn cta-primary">View our products</a>
  <a class="abs cta-link">Get in touch</a>
  <div class="abs hero-terminal" role="img" aria-label="Hand tapping a betting touchscreen terminal"></div>
  <div class="abs hero-photo" role="img" aria-label="Jockeys and horses racing on a dirt track"></div>
</section>

<h2 class="abs section-title">Our Products</h2>
<p class="abs section-sub">Neque egestas congue quisque egestas diam in. Semper quis lectus nulla at volutpat diam ut venenatis.</p>

<!-- Point of Sale -->
<section>
  <h3 class="abs product-title" style="left:30px;top:1240px">Point of Sale</h3>
  <p class="abs product-copy" style="left:30px;top:1316px">Lorem ipsum dolor sit amet, consectetur adipiscing elit, sed do eiusmod tempor incididunt ut labore et dolore magna aliqua.</p>
  <div class="abs features" style="left:40px;top:1402px">
    <div class="feature"><svg viewBox="0 0 48 48" fill="none" stroke="#444" stroke-width="2.5" stroke-linecap="round"><path d="M42 22v2A18 18 0 1 1 31 7.5"/><path d="M16 23l7 7L43 9"/></svg>Key Feature 1</div>
    <div class="feature"><svg viewBox="0 0 48 48" fill="none" stroke="#444" stroke-width="2.5"><circle cx="24" cy="24" r="20"/><path d="M29 5L18 24M41 14H19M40 34L29 15M24 44L35 24M7 34h22M8 14l11 19"/></svg>Key Feature 2</div>
    <div class="feature"><svg viewBox="0 0 48 48" fill="none" stroke="#444" stroke-width="2.5" stroke-linejoin="round"><circle cx="24" cy="17" r="13"/><path d="M16 27l-3 18 11-6 11 6-3-18"/></svg>Key Feature 3</div>
  </div>
  <a class="abs btn more" style="left:30px;top:1577px">More information</a>

  <svg class="abs" style="left:1112px;top:1280px" width="60" height="210" aria-hidden="true">
    <g fill="var(--dot)"><circle cx="5" cy="4" r="2"/><circle cx="30" cy="4" r="2"/><circle cx="55" cy="4" r="2"/><circle cx="5" cy="29" r="2"/><circle cx="30" cy="29" r="2"/><circle cx="55" cy="29" r="2"/><circle cx="5" cy="54" r="2"/><circle cx="30" cy="54" r="2"/><circle cx="55" cy="54" r="2"/><circle cx="5" cy="79" r="2"/><circle cx="30" cy="79" r="2"/><circle cx="55" cy="79" r="2"/><circle cx="5" cy="104" r="2"/><circle cx="30" cy="104" r="2"/><circle cx="55" cy="104" r="2"/><circle cx="55" cy="129" r="2"/><circle cx="55" cy="154" r="2"/><circle cx="55" cy="179" r="2"/><circle cx="55" cy="204" r="2"/></g>
  </svg>

  <div class="abs card" style="left:732px;top:1186px;width:370px;height:407px">
    <div class="card-head">Session By Channel</div>
    <svg class="abs" style="left:104px;top:80px" width="160" height="160" viewBox="0 0 160 160">
      <g fill="none" stroke-width="30" transform="rotate(-90 80 80)">
        <circle cx="80" cy="80" r="63" stroke="var(--blue)"/>
        <circle cx="80" cy="80" r="63" stroke="var(--teal)" stroke-dasharray="0 165 60 400"/>
        <circle cx="80" cy="80" r="63" stroke="var(--orange)" stroke-dasharray="0 100 70 400"/>
        <circle cx="80" cy="80" r="63" stroke="var(--red)" stroke-dasharray="0 0 100 400"/>
      </g>
      <text x="80" y="80" text-anchor="middle" font-family="Poppins,sans-serif" font-size="18" font-weight="600" fill="#222">82%</text>
      <text x="80" y="96" text-anchor="middle" font-family="Poppins,sans-serif" font-size="9" fill="#999">Reached</text>
    </svg>
    <div class="abs" style="left:0;top:270px;width:100%;border-top:1px solid var(--line)"></div>
    <div class="abs small" style="left:17px;top:295px">ORGANIC</div>
    <div class="abs" style="left:17px;top:317px;font-size:13px;font-weight:600;color:#222"><span style="color:var(--orange)">●</span>&nbsp; 2,345</div>
    <div class="abs small" style="left:17px;top:352px">REFFERAL</div>
    <div class="abs" style="left:17px;top:374px;font-size:13px;font-weight:600;color:#222"><span style="color:var(--blue)">●</span>&nbsp; 2,345</div>
  </div>

  <div class="abs card" style="left:784px;top:1403px;width:368px;height:287px">
    <div class="abs" style="left:23px;top:21px;font-size:14.5px;font-weight:600;color:var(--ink)">Acquisition</div>
    <div class="abs small" style="left:23px;top:51px;width:320px;line-height:13px">Tells you where your visitors originated from, such as search engines, social networks or website referrals.</div>
    <svg class="abs" style="left:23px;top:130px" width="324" height="135" viewBox="0 0 324 135">
      <path d="M0 10L15 22 30 20 45 10 60 20 80 20 95 2 110 2 140 14 160 12 180 6 200 22 220 12 240 14 255 8 270 22 285 26 300 22 322 26V135H0Z" fill="#f3f5fa"/>
      <polyline points="0,10 15,22 30,20 45,10 60,20 80,20 95,2 110,2 140,14 160,12 180,6 200,22 220,12 240,14 255,8 270,22 285,26 300,22 322,26" fill="none" stroke="#999" stroke-width="1.2"/>
      <path d="M0 105L15 95 30 80 45 82 60 88 80 85 95 90 115 75 140 70 160 55 180 62 200 70 220 65 240 58 255 50 270 55 285 68 300 70 322 55V135H0Z" fill="#e8ecfb"/>
      <polyline points="0,105 15,95 30,80 45,82 60,88 80,85 95,90 115,75 140,70 160,55 180,62 200,70 220,65 240,58 255,50 270,55 285,68 300,70 322,55" fill="none" stroke="var(--blue)" stroke-width="1.5"/>
    </svg>
  </div>
</section>

<!-- Self-Service Terminals -->
<section>
  <svg class="abs" style="left:413px;top:1866px" width="85" height="215" aria-hidden="true">
    <g fill="var(--dot)"><circle cx="4" cy="4" r="2"/><circle cx="29" cy="4" r="2"/><circle cx="54" cy="4" r="2"/><circle cx="79" cy="4" r="2"/><circle cx="4" cy="29" r="2"/><circle cx="29" cy="29" r="2"/><circle cx="54" cy="29" r="2"/><circle cx="79" cy="29" r="2"/><circle cx="4" cy="54" r="2"/><circle cx="29" cy="54" r="2"/><circle cx="54" cy="54" r="2"/><circle cx="79" cy="54" r="2"/><circle cx="4" cy="79" r="2"/><circle cx="29" cy="79" r="2"/><circle cx="54" cy="79" r="2"/><circle cx="79" cy="79" r="2"/><circle cx="54" cy="104" r="2"/><circle cx="79" cy="104" r="2"/><circle cx="54" cy="129" r="2"/><circle cx="79" cy="129" r="2"/><circle cx="54" cy="154" r="2"/><circle cx="79" cy="154" r="2"/><circle cx="54" cy="179" r="2"/><circle cx="79" cy="179" r="2"/><circle cx="54" cy="204" r="2"/><circle cx="79" cy="204" r="2"/></g>
  </svg>

  <div class="abs card" style="left:32px;top:1814px;width:370px;height:334px">
    <div class="abs" style="left:19px;top:18px;font-size:14.5px;font-weight:600;color:var(--ink)">Agent Performance Points</div>
    <div class="abs" role="img" aria-label="Agent avatar" style="left:19px;top:66px;width:39px;height:39px;border-radius:50%;background:#d8b48e"></div>
    <div class="abs" style="left:68px;top:68px;font-size:11px;font-weight:600;color:#222">Lorem ipsum dolor</div>
    <div class="abs small" style="left:68px;top:86px">Technical Support</div>
    <div class="abs" style="left:326px;top:72px;width:9px;height:9px;border-radius:50%;background:var(--blue)"></div>
    <div class="abs" style="left:68px;top:110px;width:268px;height:3px;background:#e9ecf3;border-radius:2px"><div style="width:196px;height:3px;background:var(--blue);border-radius:2px"></div></div>
    <div class="abs" style="left:68px;top:120px;font-size:11px;color:#222">Executive Level</div>
    <div class="abs" style="left:272px;top:120px;font-size:11px;color:#222">213,435,890</div>
    <div class="abs" role="img" aria-label="Agent avatar" style="left:19px;top:152px;width:39px;height:39px;border-radius:50%;background:#e3a89a"></div>
    <div class="abs" role="img" aria-label="Agent avatar" style="left:19px;top:238px;width:39px;height:39px;border-radius:50%;background:#1f6f86"></div>
  </div>

  <div class="abs card" style="left:86px;top:1958px;width:369px;height:289px">
    <div class="card-head">Device Session</div>
    <div class="abs small" style="left:18px;top:78px"><span style="color:var(--blue)">●</span>&nbsp; MOBILE</div>
    <div class="abs small" style="left:118px;top:78px"><span style="color:#e07a5f">●</span>&nbsp; DESKTOP</div>
    <div class="abs small" style="left:219px;top:78px"><span style="color:#ccc">●</span>&nbsp; OTHER</div>
    <div class="abs" style="left:37px;top:98px;font-size:13px;font-weight:600;color:#222">4,345</div>
    <div class="abs" style="left:138px;top:98px;font-size:13px;font-weight:600;color:#222">4,345</div>
    <div class="abs" style="left:239px;top:98px;font-size:13px;font-weight:600;color:#222">4,345</div>
    <svg class="abs" style="left:10px;top:128px" width="350" height="155" viewBox="0 0 350 155">
      <g stroke="#eef0f4"><line x1="8" y1="0" x2="8" y2="122"/><line x1="50" y1="0" x2="50" y2="122"/><line x1="92" y1="0" x2="92" y2="122"/><line x1="134" y1="0" x2="134" y2="122"/><line x1="176" y1="0" x2="176" y2="122"/><line x1="218" y1="0" x2="218" y2="122"/><line x1="260" y1="0" x2="260" y2="122"/><line x1="302" y1="0" x2="302" y2="122"/><line x1="346" y1="0" x2="346" y2="122"/><line x1="8" y1="122" x2="346" y2="122"/></g>
      <path d="M8 82L25 92 45 78 70 80 95 78 110 70 135 55 155 25 180 30 200 38 225 42 240 35 258 12 275 22 290 50 310 58 330 50 346 28V122H8Z" fill="#ecfafc"/>
      <polyline points="8,82 25,92 45,78 70,80 95,78 110,70 135,55 155,25 180,30 200,38 225,42 240,35 258,12 275,22 290,50 310,58 330,50 346,28" fill="none" stroke="#7fdbe8" stroke-width="1.4"/>
      <polyline points="8,98 18,104 30,95 50,96 70,98 90,98 115,94 140,84 160,74 178,76 200,68 215,80 225,92 240,78 260,78 275,70 290,78 305,82 325,70 346,62" fill="none" stroke="var(--blue)" stroke-width="1.6"/>
      <g font-family="Poppins,sans-serif" font-size="10" fill="#777" text-anchor="middle"><text x="8" y="146">10</text><text x="50" y="146">20</text><text x="92" y="146">30</text><text x="134" y="146">40</text><text x="176" y="146">50</text><text x="218" y="146">60</text><text x="260" y="146">70</text><text x="302" y="146">80</text><text x="346" y="146">90</text></g>
    </svg>
  </div>

  <h3 class="abs product-title" style="left:619px;top:1840px">Self-Service Terminals</h3>
  <p class="abs product-copy" style="left:619px;top:1908px">Lorem ipsum dolor sit amet, consectetur adipiscing elit, sed do eiusmod tempor incididunt ut labore et dolore magna aliqua.</p>
  <div class="abs features" style="left:630px;top:1993px;gap:20px">
    <div class="feature"><svg viewBox="0 0 48 48" fill="none" stroke="#444" stroke-width="2.5" stroke-linecap="round"><path d="M42 22v2A18 18 0 1 1 31 7.5"/><path d="M16 23l7 7L43 9"/></svg>Key Feature 1</div>
    <div class="feature"><svg viewBox="0 0 48 48" fill="none" stroke="#444" stroke-width="2.5"><circle cx="24" cy="24" r="20"/><path d="M29 5L18 24M41 14H19M40 34L29 15M24 44L35 24M7 34h22M8 14l11 19"/></svg>Key Feature 2</div>
    <div class="feature"><svg viewBox="0 0 48 48" fill="none" stroke="#444" stroke-width="2.5" stroke-linejoin="round"><circle cx="24" cy="17" r="13"/><path d="M16 27l-3 18 11-6 11 6-3-18"/></svg>Key Feature 3</div>
  </div>
  <a class="abs btn more" style="left:619px;top:2168px">More information</a>
</section>

</body>
</html>
```